Promotional Double-Sided postcard

We are promoting a web cam studio (www.velmorastudio.com) and making a postcard for recruiting models. I have attached a .doc of a very basic 8.5x11 flyer we drew up which contains the same information we want conveyed in the postcard. I've also attached our website's logo.

Industry/Entity Type

Promotional

```html
<!DOCTYPE html>
<html lang="en">
<head>
<meta charset="utf-8">
<title>Velmora Studio – Model Recruiting Postcard</title>
<link rel="stylesheet" href="https://fonts.googleapis.com/css2?family=Arimo:wght@400;700&family=Open+Sans:ital,wght@0,600;0,700;0,800;1,800&display=swap">
<style>
  :root {
    --page-bg: #eceeed;
    --magenta: #e0177f;
    --magenta-deep: #8a0f55;
    --plum-dark: #22060f;
    --white: #ffffff;
    --ink: #333333;
    --rule: #555555;
    --card-edge: #2b2b30;
  }
  * { margin: 0; padding: 0; box-sizing: border-box; }
  html, body { width: 754px; height: 1200px; overflow: hidden; background: var(--page-bg); }
  body { position: relative; font-family: "Arimo", Arial, sans-serif; }

  .postcard-front {
    position: absolute; left: 19px; top: 23px; width: 716px; height: 551px;
    border-bottom: 4px solid var(--card-edge); overflow: hidden;
  }
  .front-photo {
    position: absolute; inset: 0;
    background: linear-gradient(180deg, #d9d8e4 0%, #a9a8bd 25%, #6e6c86 50%, #3b3956 72%, #17162a 100%);
  }
  .brand-mark {
    position: absolute; left: 30px; top: 52px; display: flex; align-items: center; gap: 8px;
    font-family: "Open Sans", sans-serif; font-weight: 800; font-size: 19px; color: var(--magenta);
  }
  .brand-mark .dot { width: 22px; height: 22px; border-radius: 50%; background: var(--magenta); }

  .pay-headline {
    position: absolute; left: 60px; top: 290px; width: 300px; text-align: right;
    font-family: "Open Sans", sans-serif; color: var(--white);
  }
  .pay-amount {
    display: block; font-size: 66px; line-height: 60px; font-weight: 800; font-style: italic; letter-spacing: -1px;
    color: var(--magenta); -webkit-text-stroke: 2px var(--white); paint-order: stroke fill;
  }
  .pay-period { display: block; font-size: 32px; line-height: 32px; font-weight: 700; margin-top: -2px; }
  .pitch {
    position: absolute; left: 39px; top: 398px; width: 320px;
    font-size: 13.4px; line-height: 18.3px; color: var(--white); text-align: justify;
  }
  .offer {
    position: absolute; right: 29px; top: 327px; width: 320px; text-align: right;
    font-family: "Arimo", Arial, sans-serif; font-weight: 700; font-size: 13.4px; line-height: 16.4px;
    color: var(--white);
  }
  .perks {
    position: absolute; right: 35px; top: 404px; width: 300px; text-align: right; list-style: none;
    font-family: "Arimo", Arial, sans-serif; font-weight: 700; font-size: 10.6px; line-height: 16.1px;
    color: var(--white); padding-right: 4px; border-right: 8px solid var(--magenta);
  }

  .postcard-back {
    position: absolute; left: 19px; top: 607px; width: 716px; height: 551px; background: var(--white);
  }
  .back-promo {
    position: absolute; left: 0; top: 0; width: 348px; height: 551px;
    background: linear-gradient(180deg, #c0176f 0%, #d61c84 40%, #a0105f 62%, #4a0828 85%, var(--plum-dark) 100%);
  }
  .promo-band { position: absolute; left: 0; top: 0; width: 348px; height: 34px;
    background: linear-gradient(90deg, #b81570, var(--magenta-deep)); }
  .model-strip { position: absolute; top: 35px; height: 114px; background: var(--white); left: 0; width: 348px; }
  .model-photo { position: absolute; top: 0; height: 114px; }
  .model-photo.one { left: 0; width: 92px; background: linear-gradient(160deg, #e9e4e6, #9a6f58 55%, #3a2320); }
  .model-photo.two { left: 102px; width: 83px; background: linear-gradient(160deg, #f2f0f0, #b08a78 55%, #4a3028); }
  .model-photo.three { left: 194px; width: 153px; background: linear-gradient(160deg, #f3f3f5, #c9a79a 50%, #3b2b2f); }
  .back-brand {
    position: absolute; left: 0; width: 348px; top: 258px; display: flex; justify-content: center;
    align-items: center; gap: 8px;
    font-family: "Open Sans", sans-serif; font-weight: 800; font-size: 22px; color: var(--white);
  }
  .back-brand .dot { width: 26px; height: 26px; border-radius: 50%; background: var(--white); }
  .contact {
    position: absolute; left: 0; width: 348px; top: 336px; text-align: center;
    font-family: "Open Sans", sans-serif; font-weight: 700; font-size: 18.5px; line-height: 28px;
    color: var(--white);
  }

  .mail-label { position: absolute; font-size: 21px; line-height: 26px; color: var(--ink); }
  .postage { left: 586px; top: 68px; width: 84px; text-align: center; }
  .address { left: 385px; top: 218px; }
  .barcode-label { left: 394px; top: 490px; }
  .address-lines { position: absolute; left: 387px; top: 249px; width: 291px; }
  .address-lines span { display: block; height: 30px; border-bottom: 1px solid var(--rule); }
</style>
</head>
<body>
  <section class="postcard-front">
    <div class="front-photo" role="img" aria-label="Photo: model on a red carpet facing a crowd of photographers"></div>
    <div class="brand-mark"><span class="dot"></span>Velmora Studio</div>

    <h1 class="pay-headline">
      <span class="pay-amount">$3000</span>
      <span class="pay-period">every month</span>
    </h1>
    <p class="pitch">That is a realistic number you can earn average working part-time as a live webcam model. Some full time models make that much in a WEEK, but think of what you could do with just an extra $3000 a month! If you've been given this flyer, it's because YOU could be making great money as a live webcam model.</p>

    <p class="offer">From the comfort of your home or in our<br>Beverly Hills cam studio,<br>we will help you discover one of the<br>most lucrative yet flexible jobs there is.</p>
    <ul class="perks">
      <li>* Free photo shoots for all models.</li>
      <li>* Artistic freedom.&nbsp; Nudity is entirely up to you.</li>
      <li>* Block anyone in Los Angeles</li>
      <li>from ever seeing you online.</li>
      <li>* Friendly staff with studio access</li>
      <li>available 24 hours a day, 7 days a week</li>
    </ul>
  </section>

  <section class="postcard-back">
    <div class="back-promo">
      <div class="promo-band"></div>
      <div class="model-strip">
        <div class="model-photo one" role="img" aria-label="Portrait photo of a model"></div>
        <div class="model-photo two" role="img" aria-label="Portrait photo of a model"></div>
        <div class="model-photo three" role="img" aria-label="Portrait photo of a model"></div>
      </div>
      <div class="back-brand"><span class="dot"></span>Velmora Studio</div>
      <p class="contact">Visit our website at<br>www.velmorastudio.com<br>to contact us with<br>any questions.<br>or Call 12345678910</p>
    </div>

    <p class="mail-label postage">Postage<br>Area</p>
    <p class="mail-label address">AddressArea</p>
    <div class="address-lines"><span></span><span></span><span></span><span></span></div>
    <p class="mail-label barcode-label">Barcode Area</p>
  </section>
</body>
</html>
```